Fleur Vallon Riding School Flyer Design

We need a flyer for our Horse riding school, called Fleur Vallon Riding School.

At Fleur Vallon Riding School, Horses and ponies are carefully matched to suit each rider's experience, ability and confidence. I am a Qualified instructor, equipped to train all levels from nervous beginners to the more advanced.

Horse riding is fun! Riders, particularly children, are taught not only skills on the horse, but skills that are integral to good horsemanship and ownership of horses.

We regularly host Ladies Days, Guest Instructors, 1 hour Trail Rides and Pony Ride Days!

We teach people how to interact safely with, and care for horses so they develop a genuine love and respect for the animals and the sport.

In addition to fundamental riding techniques including walk, trot, and canter, we teach our students:
Grooming and Care of horses, Safety around horses, Balance and Co-Ordination, How to saddle up and care for Tack, Responsibility for equipment and horse, Confidence and Confidence Building for all Ages.

Private and group lessons start at 5 years of age upwards.

We recommend children 4 years and under partake in 15 minute pony rides, mainly due to their attention span!

```html
<!DOCTYPE html>
<html lang="en">
<head>
<meta charset="utf-8">
<title>Fleur Vallon Riding School Flyer</title>
<link href="https://fonts.googleapis.com/css2?family=Lato:wght@400;700&family=Arimo:wght@700&display=swap" rel="stylesheet">
<style>
  :root {
    --forest: #434d41;
    --white: #ffffff;
    --red: #e3222a;
    --ink: #1c1c1c;
    --badge: #1e1e1e;
    --page: #e9e9e6;
  }
  * { margin: 0; padding: 0; box-sizing: border-box; }
  html, body { width: 1200px; height: 900px; overflow: hidden; background: var(--page); }
  .flyer {
    position: absolute; left: 85px; top: 82px;
    width: 1030px; height: 730px;
    background: var(--forest); overflow: hidden;
    font-family: "Lato", sans-serif; color: var(--white);
    box-shadow: 0 6px 18px rgba(0,0,0,.25);
  }
  .flyer-shapes { position: absolute; left: 0; top: 0; display: block; }
  .offer-badge {
    position: absolute; left: 30px; top: 243px; width: 170px; height: 170px;
    border-radius: 50%; background: var(--badge); border: 5px solid var(--white);
    display: flex; flex-direction: column; align-items: center; justify-content: center;
    text-align: center; line-height: 1.1;
  }
  .offer-badge .offer-hours { color: var(--red); font-size: 30px; }
  .offer-badge .offer-main { font-size: 21px; }
  .offer-badge .offer-sub { font-size: 16px; margin-top: 2px; }
  .rider-photo {
    position: absolute; left: 497px; top: 248px; width: 216px; height: 216px;
    border-radius: 50%; border: 6px solid var(--white);
    background: radial-gradient(circle at 62% 72%, #5a3a24 0 32%, transparent 58%),
                linear-gradient(180deg, #8fc7ef 0%, #b9dcf3 45%, #2c3550 100%);
  }
  .school-name { position: absolute; left: 741px; top: 200px; width: 280px; text-align: center; color: var(--ink); }
  .school-name .name-dot { width: 70px; height: 70px; border-radius: 50%; border: 2px solid var(--ink); margin: 0 auto 38px; }
  .school-name .name-main { font-size: 27px; letter-spacing: 4px; line-height: 1; }
  .school-name .name-sub { font-size: 14px; letter-spacing: 3px; margin-top: 14px; line-height: 1; }
  .label-box {
    position: absolute; background: var(--white); font-weight: 700; font-size: 26px;
    display: flex; align-items: center; justify-content: center;
  }
  .label-provide { left: 0; top: 440px; width: 217px; height: 40px; color: var(--forest); }
  .label-about { left: 845px; top: 426px; width: 185px; height: 45px; color: var(--red); }
  .provide-list {
    position: absolute; left: 40px; top: 498px; width: 440px;
    list-style: none; display: grid; grid-template-columns: 210px 230px; row-gap: 9px;
    font-size: 27px; line-height: 34px;
  }
  .provide-list li::before { content: "•"; margin-right: 18px; }
  .lessons-box {
    position: absolute; left: 0; top: 598px; width: 530px; height: 80px;
    background: var(--white); padding: 11px 0 0 30px;
    font-family: "Arimo", sans-serif; font-weight: 700; line-height: 1.15;
  }
  .lessons-box .lessons-line { color: var(--ink); font-size: 22px; }
  .lessons-box .lessons-age { color: var(--red); font-size: 28px; letter-spacing: .3px; }
  .about-text {
    position: absolute; left: 533px; top: 483px; width: 467px;
    font-size: 16.5px; line-height: 23px; text-align: justify; text-align-last: right;
  }
  .events-line {
    position: absolute; right: 30px; top: 608px; text-align: right;
    font-family: "Arimo", sans-serif; font-weight: 700; font-size: 27px; line-height: 1.15;
  }
</style>
</head>
<body>
  <main class="flyer">
    <svg class="flyer-shapes" viewBox="0 0 1030 730" width="1030" height="730">
      <defs>
        <linearGradient id="horse-photo-tone" x1="0" y1="0" x2="1" y2="1">
          <stop offset="0" stop-color="#8a8760"/>
          <stop offset=".45" stop-color="#9c6a3c"/>
          <stop offset="1" stop-color="#6c6a4c"/>
        </linearGradient>
      </defs>
      <rect class="hero-photo" role="img" aria-label="Photo of a chestnut horse with a white blaze wearing a bridle" x="0" y="0" width="1030" height="480" fill="url(#horse-photo-tone)"/>
      <!-- left band behind the badge -->
      <path class="band-left-white" d="M0,298 C150,288 310,345 405,470 L0,470 Z" fill="var(--white)"/>
      <path class="band-left-green" d="M0,298 C110,290 180,310 220,330 C170,318 90,330 0,372 Z" fill="var(--forest)"/>
      <path class="band-left-green" d="M0,298 C120,292 190,315 230,342 L190,350 C130,340 60,350 0,370 Z" fill="var(--forest)"/>
      <path class="band-left-line" d="M205,346 C290,366 350,405 405,468" fill="none" stroke="var(--forest)" stroke-width="6"/>
      <!-- right swoosh -->
      <path class="swoosh-white" d="M405,470 C560,350 790,130 1030,43 L1030,410 C800,400 600,420 405,470 Z" fill="var(--white)"/>
      <path class="swoosh-stripe" d="M470,426 C650,300 850,165 1030,128 L1030,144 C855,180 665,312 482,436 Z" fill="var(--forest)"/>
      <!-- lower panel, one piece -->
      <path class="panel-lower" d="M0,392 C200,384 330,425 405,470 C600,420 800,400 1030,405 L1030,730 L0,730 Z" fill="var(--forest)"/>
    </svg>

    <div class="offer-badge">
      <span class="offer-hours">1 HOUR</span>
      <span class="offer-main">TRAIL RIDES</span>
      <span class="offer-sub">AND PONY RIDE</span>
    </div>

    <div class="rider-photo" role="img" aria-label="Photo of a young rider in a helmet on a bay horse"></div>

    <div class="school-name">
      <div class="name-dot"></div>
      <div class="name-main">FLEUR VALLON</div>
      <div class="name-sub">RIDING SCHOOL</div>
    </div>

    <div class="label-box label-provide">WE PROVIDE</div>
    <ul class="provide-list">
      <li>Grooming</li>
      <li>Balance</li>
      <li>Safety</li>
      <li>Co-ordination</li>
    </ul>

    <div class="lessons-box">
      <div class="lessons-line">PRIVATE AND GROUP LESSONS START</div>
      <div class="lessons-age">AT 5 YEARS OF AGE UPWARDS</div>
    </div>

    <div class="label-box label-about">ABOUT US</div>
    <p class="about-text">At Fleur Vallon Riding School, Horses and ponies are carefully matched to suit each rider's experience, ability and confidence. I am a Qualified instructor, equipped to train all levels from nervous beginners to the more advanced.</p>
    <p class="events-line">We regularly host Ladies Days,<br>Guest Instructors</p>
  </main>
</body>
</html>
```